Kestrel Hitches Square Business Card Design

I would like a 2 x 2 square rounded corner business card.my business manufacture vehicle hitches and uses square tubing with rounded corners and would like to incorporate the border to look like the tubing...
4127 Larkfield Ave. Millbrook, Ohio 44098
(731) 555-0187
dale@kestrelhitches.example
www.kestrelhitches.example

Target Market(s)

automotive / vehicle hitches

Industry/Entity Type

Automotive

Contact Information for Business Card

I would like a 2 x 2 square rounded corner business card.my business manufacture vehicle hitches and uses square tubing with rounded corners and would like to incorporate the border to look like the tubing... and red, white and blue theme colors

Font styles to use
Sans Serif

Colors

Designer to choose colors to be used in the design.

Requirements
Must have
• Boarder
Nice to have
• red, white, blue theme colors
Should not have
• odd colors

```html
<!DOCTYPE html>
<html lang="en">
<head>
<meta charset="utf-8">
<title>Kestrel Hitches – Square Business Card</title>
<link rel="stylesheet" href="https://fonts.googleapis.com/css2?family=Open+Sans:wght@400;700&family=Arimo&display=swap">
<style>
  :root {
    --navy: #1b3a6e;
    --red: #e21f2f;
    --white: #ffffff;
    --bg-light: #cfd0d3;
    --bg-dark: #76777b;
    --steel-dark: #4a4b4f;
    --steel-mid: #8e9095;
    --steel-light: #f4f4f6;
  }
  html, body {
    margin: 0;
    width: 1200px;
    height: 1000px;
    overflow: hidden;
  }
  body {
    position: relative;
    background: radial-gradient(ellipse 700px 620px at 50% 45%, var(--bg-light) 0%, #a3a4a8 55%, var(--bg-dark) 100%);
    font-family: "Open Sans", sans-serif;
  }
  .card {
    position: absolute;
    top: 265px;
    width: 470px;
    height: 470px;
    box-sizing: border-box;
    padding: 29px;
    border-radius: 74px;
    background: linear-gradient(160deg, var(--steel-dark) 0%, var(--steel-light) 14%, var(--steel-mid) 32%, #d9dadd 50%, var(--steel-dark) 70%, var(--steel-light) 86%, var(--steel-mid) 100%);
    box-shadow: inset 0 0 0 2px #5a5b5f, 0 2px 6px rgba(0,0,0,.25);
  }
  .card--front { left: 110px; }
  .card--back { left: 620px; }
  .tube-inner {
    width: 100%;
    height: 100%;
    box-sizing: border-box;
    padding: 31px;
    border-radius: 52px;
    background: linear-gradient(20deg, var(--steel-mid) 0%, var(--steel-light) 18%, #5c5d61 40%, #e6e7ea 58%, var(--steel-mid) 78%, var(--steel-light) 100%);
    box-shadow: inset 0 0 0 3px #3f4044, 0 0 0 2px #e8e8ea;
  }
  .face {
    width: 100%;
    height: 100%;
    box-sizing: border-box;
    border-radius: 28px;
    background: var(--white);
    box-shadow: 0 0 0 3px #dcdcde, 0 0 0 5px #5a5b5f;
    text-align: center;
    position: relative;
  }
  .face > * {
    position: absolute;
    left: 0;
    right: 0;
    margin: 0;
  }
  .brand-name {
    color: var(--navy);
    font-weight: 700;
  }
  .card--front .brand-name {
    top: 56px;
    font-size: 36px;
    line-height: 38px;
  }
  .card--back .brand-name {
    top: 156px;
    font-size: 58px;
    line-height: 57px;
  }
  .person-name {
    top: 153px;
    color: var(--navy);
    font-weight: 700;
    font-size: 25px;
    line-height: 30px;
  }
  .person-title {
    top: 182px;
    color: var(--red);
    font-size: 18px;
    line-height: 24px;
  }
  .contact {
    top: 221px;
    font-family: "Arimo", sans-serif;
    font-style: normal;
    font-size: 19px;
    line-height: 24px;
    color: var(--navy);
  }
</style>
</head>
<body>
  <section class="card card--front">
    <div class="tube-inner">
      <div class="face">
        <h1 class="brand-name">Kestrel<br>Hitches</h1>
        <p class="person-name">Dale R. Whitcombe</p>
        <p class="person-title">Owner</p>
        <address class="contact">
          4127 Larkfield Ave.<br>
          Millbrook, Ohio 44098<br>
          (731) 555-0187<br>
          dale@kestrelhitches.example<br>
          www.kestrelhitches.example
        </address>
      </div>
    </div>
  </section>

  <section class="card card--back">
    <div class="tube-inner">
      <div class="face">
        <h2 class="brand-name">Kestrel<br>Hitches</h2>
      </div>
    </div>
  </section>
</body>
</html>
```